I have a transportation trucking company and I’m expanding and hiring drivers

I need a flyer for my social media to let people know I’m hiring and looking for drivers , Please incorporate my company logo and i need to flyer to give some information about the position, I will upload some examples,

I do need it to say We are hiring!
We are looking for CDL- Class A Drivers
2 Years Minimum Driving Experience
Percentage Pay
Clean Driving Record
No Violations or accidents
Weekly Direct Deposit
Sign On bonus
Holiday Bonus
Detention/ Layover Pay
Must Stay out a minimum of 2 full weeks

Interested in more information?
Email info@maplecresthaul.com
(555) 218-6093

Maplecrest Haul LLC
824 Linden Ferry Lane Suite 200 Jenkintown PA 19000

Industry/Entity Type

Long Distance Trucking

Font styles to use
Serif
Sans Serif
Decorative
Script

Requirements
Must have
• Please incorporate my logo into the flyer

Please have just the flyer take up the whole canvas this will be printed and posted on our social media’s
Nice to have

```html
<!DOCTYPE html>
<html lang="en">
<head>
<meta charset="UTF-8">
<title>Maplecrest Haul LLC – We Are Hiring</title>
<link href="https://fonts.googleapis.com/css2?family=Montserrat:wght@600;700;800&display=swap" rel="stylesheet">
<style>
  :root {
    --blue: #2a62b3;
    --dark: #333436;
    --white: #ffffff;
    --paper: #f1f2f4;
    --photo-grey: #8f9396;
    --photo-red: #9a3a3c;
  }
  * { margin: 0; padding: 0; box-sizing: border-box; }
  html, body { width: 900px; height: 1200px; overflow: hidden; background: var(--white); }
  body { font-family: "Montserrat", Arial, sans-serif; }
  .flyer { position: relative; width: 900px; height: 1200px; overflow: hidden;
    background: linear-gradient(180deg, var(--white) 0 585px, var(--paper) 585px, #fafafb 800px, var(--paper) 1035px); }
  .shapes { position: absolute; inset: 0; }
  .brand { position: absolute; left: 20px; width: 400px; top: 72px; text-align: center; color: var(--blue); font-weight: 800; }
  .brand-mark { width: 104px; height: 104px; background: var(--blue); margin: 0 auto 34px; }
  .brand-name { font-size: 56px; line-height: 1; letter-spacing: 1px; }
  .brand-sub { font-size: 16px; letter-spacing: 9px; margin-top: 10px; }
  .we-are { position: absolute; left: 54px; top: 334px; width: 307px; height: 70px; background: var(--dark);
    color: var(--white); font-weight: 800; font-size: 62px; line-height: 70px; text-align: center; letter-spacing: 1px; }
  .hiring { position: absolute; left: 46px; top: 400px; color: var(--white); font-weight: 800; font-size: 124px; line-height: 1.05; letter-spacing: -1px; }
  .role { position: absolute; left: 127px; top: 540px; width: 646px; height: 60px; background: var(--dark);
    border-radius: 40px 40px 0 0; color: var(--white); font-weight: 700; font-size: 38px; line-height: 62px; text-align: center; }
  .requirements { position: absolute; left: 59px; top: 660px; list-style: none; }
  .requirements li { display: flex; align-items: center; height: 39.6px; font-size: 29px; font-weight: 700; color: var(--dark); }
  .requirements svg { width: 30px; height: 30px; margin-right: 20px; flex: none; }
  .address { position: absolute; left: 0; top: 1035px; width: 900px; height: 76px; background: var(--blue);
    color: var(--white); text-align: center; font-weight: 700; font-size: 20.5px; line-height: 28px; padding-top: 10px; }
  .contact { position: absolute; left: 0; top: 1111px; width: 900px; height: 89px; background: var(--dark);
    color: var(--white); text-align: center; font-weight: 700; font-size: 20.5px; line-height: 28px; padding-top: 16px; }
</style>
</head>
<body>
<div class="flyer">
  <svg class="shapes" width="900" height="1200" viewBox="0 0 900 1200">
    <defs>
      <linearGradient id="roadPhoto" x1="0" y1="0" x2="1" y2="1">
        <stop offset="0" stop-color="#b9bcbd"/>
        <stop offset="0.5" stop-color="var(--photo-grey)"/>
        <stop offset="0.75" stop-color="var(--photo-red)"/>
        <stop offset="1" stop-color="#3e4144"/>
      </linearGradient>
      <linearGradient id="fieldPhoto" x1="0" y1="0" x2="0" y2="1">
        <stop offset="0" stop-color="#e7b9a8"/>
        <stop offset="0.45" stop-color="#c98a7a"/>
        <stop offset="0.6" stop-color="#6f8a4e"/>
        <stop offset="1" stop-color="#4a5f3a"/>
      </linearGradient>
    </defs>
    <polygon points="0,413 560,413 810,568 900,521 900,585 0,585" fill="var(--blue)"/>
    <polygon role="img" aria-label="Photo of a container truck driving under a concrete highway overpass"
      points="455,0 900,0 900,521 810,568 455,348" fill="url(#roadPhoto)"/>
    <polyline points="455,348 810,568 900,521" fill="none" stroke="var(--white)" stroke-width="5"/>
    <polygon points="737,674 870,750 870,904 737,980 604,904 604,750" fill="var(--dark)"/>
    <polygon role="img" aria-label="Photo of a red truck on a country road at sunset"
      points="737,686 860,756 860,898 737,968 614,898 614,756" fill="url(#fieldPhoto)"/>
  </svg>

  <div class="brand">
    <div class="brand-mark"></div>
    <div class="brand-name">MAPLECREST</div>
    <div class="brand-sub">HAUL LLC</div>
  </div>

  <div class="we-are">WE ARE</div>
  <div class="hiring">HIRING!</div>
  <div class="role">CDL-CLASS A DRIVERS</div>

  <ul class="requirements">
    <li><svg viewBox="0 0 30 30"><rect width="30" height="30" rx="5" fill="var(--blue)"/><path d="M8 15.5l5 5 9-10" fill="none" stroke="#fff" stroke-width="3.2"/></svg>2 Years Minimum Driving Experience</li>
    <li><svg viewBox="0 0 30 30"><rect width="30" height="30" rx="5" fill="var(--blue)"/><path d="M8 15.5l5 5 9-10" fill="none" stroke="#fff" stroke-width="3.2"/></svg>Percentage Pay</li>
    <li><svg viewBox="0 0 30 30"><rect width="30" height="30" rx="5" fill="var(--blue)"/><path d="M8 15.5l5 5 9-10" fill="none" stroke="#fff" stroke-width="3.2"/></svg>Clean Driving Record</li>
    <li><svg viewBox="0 0 30 30"><rect width="30" height="30" rx="5" fill="var(--blue)"/><path d="M8 15.5l5 5 9-10" fill="none" stroke="#fff" stroke-width="3.2"/></svg>No Violations or accidents</li>
    <li><svg viewBox="0 0 30 30"><rect width="30" height="30" rx="5" fill="var(--blue)"/><path d="M8 15.5l5 5 9-10" fill="none" stroke="#fff" stroke-width="3.2"/></svg>Weekly Direct Deposit</li>
    <li><svg viewBox="0 0 30 30"><rect width="30" height="30" rx="5" fill="var(--blue)"/><path d="M8 15.5l5 5 9-10" fill="none" stroke="#fff" stroke-width="3.2"/></svg>Sign On bonus</li>
    <li><svg viewBox="0 0 30 30"><rect width="30" height="30" rx="5" fill="var(--blue)"/><path d="M8 15.5l5 5 9-10" fill="none" stroke="#fff" stroke-width="3.2"/></svg>Holiday Bonus</li>
    <li><svg viewBox="0 0 30 30"><rect width="30" height="30" rx="5" fill="var(--blue)"/><path d="M8 15.5l5 5 9-10" fill="none" stroke="#fff" stroke-width="3.2"/></svg>Detention/ Layover Pay</li>
    <li><svg viewBox="0 0 30 30"><rect width="30" height="30" rx="5" fill="var(--blue)"/><path d="M8 15.5l5 5 9-10" fill="none" stroke="#fff" stroke-width="3.2"/></svg>Must Stay out a minimum of 2 full weeks</li>
  </ul>

  <div class="address">
    MAPLECREST HAUL LLC<br>
    824 Linden Ferry Lane Suite 200 Alderbrook XY 00000
  </div>
  <div class="contact">
    INTERESTED IN MORE INFORMATION?<br>
    Email info@maplecresthaul.com | (555) 218-6093
  </div>
</div>
</body>
</html>
```